New business stationairy

I need paper with header and footer and business cards.
I am a Ltd Company and my main field of expertise is QA/QC inspection in the Oil and Gas Industry. I will need all contact detail inserted and a footer with registration number and bank details etc

Industry/Entity Type

Business

```html
<!DOCTYPE html>
<html lang="en">
<head>
<meta charset="utf-8">
<title>Harwell Verification Services Ltd. – Letterhead</title>
<link rel="stylesheet" href="https://fonts.googleapis.com/css2?family=Cabin:wght@700&family=Kaushan+Script&family=Didact+Gothic&display=swap">
<style>
  :root {
    --frame-violet: #6a3cff;
    --band-light: #72e4f5;
    --band-deep: #00bfd8;
    --paper: #ffffff;
    --ink-white: #ffffff;
    --edge: #1a1a1a;
  }
  html, body {
    margin: 0;
    padding: 0;
    width: 901px;
    height: 1200px;
    overflow: hidden;
    background: var(--frame-violet);
  }
  .letterhead-frame {
    position: relative;
    width: 899px;
    height: 1198px;
    border: 1px solid var(--edge);
    background: var(--frame-violet);
  }
  .sheet {
    position: absolute;
    left: 37px;
    top: 15px;
    width: 827px;
    height: 1171px;
    background: var(--paper);
    border: 1px solid var(--edge);
    overflow: hidden;
  }
  .masthead {
    position: absolute;
    left: 0;
    top: 0;
    width: 827px;
    height: 227px;
    background: var(--band-light);
  }
  .masthead-art {
    position: absolute;
    left: 0;
    top: 0;
  }
  .masthead-rule {
    position: absolute;
    left: 0;
    bottom: 0;
    width: 827px;
    height: 33px;
    background: var(--band-deep);
  }
  .company-name {
    position: absolute;
    left: 130px;
    top: 22px;
    margin: 0;
    font-family: "Kaushan Script", cursive;
    font-weight: 400;
    font-size: 34px;
    line-height: 1;
    color: var(--ink-white);
    white-space: nowrap;
  }
  .contact-block {
    position: absolute;
    left: 145px;
    top: 72px;
    width: 320px;
    margin: 0;
    font-family: "Cabin", sans-serif;
    font-weight: 700;
    font-style: normal;
    color: var(--ink-white);
    text-align: center;
  }
  .contact-block .address-line {
    display: block;
    font-size: 16px;
    line-height: 21px;
  }
  .contact-block .reach-line {
    display: block;
    font-size: 15px;
    line-height: 20px;
  }
  .contact-block .gap { display: block; height: 3px; }
  .sheet-footer {
    position: absolute;
    left: 0;
    bottom: 0;
    width: 827px;
    height: 140px;
    background: var(--band-light);
  }
  .footer-details {
    position: absolute;
    left: 167px;
    top: 30px;
    margin: 0;
    padding: 0;
    list-style: none;
    font-family: "Didact Gothic", sans-serif;
    font-variant: small-caps;
    font-size: 17px;
    letter-spacing: 2px;
    color: var(--ink-white);
  }
  .footer-details li {
    line-height: 32px;
  }
</style>
</head>
<body>
  <div class="letterhead-frame">
    <main class="sheet">
      <header class="masthead">
        <div class="masthead-rule"></div>
        <svg class="masthead-art" width="827" height="227" viewBox="0 0 827 227">
          <defs>
            <linearGradient id="skylineTone" x1="0" y1="0" x2="0" y2="1">
              <stop offset="0" stop-color="#00bfd8" stop-opacity="0.15"/>
              <stop offset="1" stop-color="#00bfd8" stop-opacity="1"/>
            </linearGradient>
          </defs>
          <rect role="img" aria-label="Silhouette of an inspector holding a clipboard"
                x="18" y="18" width="140" height="176" rx="30" fill="#00bfd8"/>
          <rect role="img" aria-label="Silhouette of an oil refinery skyline with towers and chimneys"
                x="412" y="30" width="415" height="165" fill="url(#skylineTone)"/>
        </svg>
        <h1 class="company-name">Harwell Verification Services Ltd.</h1>
        <address class="contact-block">
          <span class="address-line">The Willows, Mill Road, Ashcombe,</span>
          <span class="address-line">Marnhull Vale</span>
          <span class="address-line">Dorset, DT9 4QX</span>
          <span class="gap"></span>
          <span class="reach-line">email: inspect.harwell@mailbox.co.uk</span>
          <span class="reach-line">mobile: 07700 900318</span>
        </address>
      </header>
      <footer class="sheet-footer">
        <ul class="footer-details">
          <li>Company registration number is:8042716</li>
          <li>Bank Name:</li>
          <li>Account No:</li>
        </ul>
      </footer>
    </main>
  </div>
</body>
</html>
```